Flyer für Photovoltaikanlagen
Zielgruppe
Aufbau bzw. unterteilung, stelle ich mir vor das es wie auf 0124_pv_aquise_a4_lws.pdf ausgelegt.
FesterBestandteile:
- Abreißkarte wie auf Flyer 1:1
- Produktfotos + Logo ( Modul KE-Lumin, QVR Batterie, Helvorn - Wechselrichter ) am besten über die Abreißkarte
- Schönes Fotos mit Dachanlage ( wenn möglich dunkele Module / Full Black Module)
- Rechnen Bsp. zur Unabhängigkeit, wie auf dem anghängten Angebot.( Seite 2 )
Inhalte die eingbaut werden sollten, wenn möglich:
Wir bauen Photovoltaikanlagen und sind Dachdeckermeisterbetrieben und Elektromeisterbetrieb (evtl. auch als Logos)
Photovoltaikanlagen Neubau / Erweiterung
- Bedarfgerechte Beratung inkl. Besichtung der Immobilie
- Transparentes Angebot
- Netzanfrage
- Markstammdatenregisterung (Vergütung für verkaufen Strom)
- Planung & Auslegung (internes Ingeneurbüro)
- Montage Dach(Dachdeckermeisterbetrieb)
- Monate Elektro inkl. Zähersetzung (Elektromeisterbetrieb)
- Einweisung ins Monitoring (App)
After Sales Service
- Service & Wartung
- Reinigung
Modern
Bedarfweckend
Produktfotos verwenden

```html
<!DOCTYPE html>
<html lang="de">
<head>
<meta charset="utf-8">
<title>Lichtwerk Solar – Flyer Photovoltaik</title>
<link href="https://fonts.googleapis.com/css2?family=Ubuntu:wght@400;500;700&display=swap" rel="stylesheet">
<style>
:root{
  --navy:#1d4170;
  --navy-2:#234a7c;
  --navy-3:#1a3a66;
  --yellow:#f2bd1d;
  --sky:#2ea3dc;
  --ink:#1b1b1b;
  --grey:#9a9da2;
  --paper:#ffffff;
  --stage:#eceeef;
}
*{box-sizing:border-box;margin:0;padding:0}
html,body{width:861px;height:1200px;overflow:hidden;background:var(--stage);font-family:'Ubuntu',sans-serif;color:var(--ink)}
.sheet-slot{position:absolute;top:310px;width:410px;height:580px;overflow:hidden;background:var(--paper)}
.slot-front{left:14px}
.slot-back{left:437px}
.sheet{position:absolute;left:0;top:0;width:680px;height:962px;transform:scale(.603);transform-origin:0 0;background:var(--paper);overflow:hidden}

/* shared */
.rule-y{position:absolute;height:4px;background:var(--yellow)}
.brand{display:flex;align-items:center;gap:6px}
.brand-dot{width:16px;height:16px;border-radius:50%;background:var(--yellow)}
.brand-name{font-weight:700;font-size:13px;color:#fff}
.contact{position:absolute;text-align:right;color:#fff;font-size:9px;line-height:1.25}
.contact b{font-weight:700}
.accent{width:36px;height:4px;background:var(--yellow);margin:12px 0 14px}
.photo{position:absolute}

/* front */
.front-head{position:absolute;left:0;top:0;width:680px;height:110px;background:var(--navy)}
.front-head .brand{position:absolute;left:48px;top:44px}
.front-head .contact{right:48px;top:44px}
.front-head-side{position:absolute;left:390px;top:110px;width:290px;height:40px;background:var(--navy)}
.hero-photo{left:48px;top:110px;width:584px;height:273px;border-radius:0 44px 0 0;
  background:linear-gradient(160deg,#f6d9b6 0%,#e79a4a 22%,#3b4b6b 45%,#2b3c5e 65%,#7a6a3a 85%,#5b7a2e 100%)}
.hero-card{position:absolute;left:48px;top:110px;width:342px;height:150px;background:#fff;border-radius:0 0 44px 0;padding:24px 0 0 20px}
.hero-card h1{font-size:29px;line-height:1.1;font-weight:700;color:var(--ink)}
.hero-card h1 span{color:var(--navy)}
.hero-card .accent{margin:14px 0 0}
.front-hero-rule{left:48px;top:383px;width:584px}
.col{position:absolute;top:406px}
.col h2{font-size:17px;line-height:1.25;font-weight:500}
.col h2 span{color:var(--navy)}
.col-why{left:48px;width:276px}
.col-why h3{font-size:10px;color:var(--navy);font-weight:500;margin:0 0 8px;line-height:1.3}
.col-why p{font-size:9.6px;line-height:1.42;text-align:justify;margin-bottom:8px}
.col-why p.lead{font-weight:500;text-align:left}
.col-steps{left:360px;width:272px}
.steps{display:grid;grid-template-columns:1fr 1fr;width:272px;height:312px}
.step{padding:22px 14px 0 20px;color:#fff}
.step:nth-child(1),.step:nth-child(4){background:var(--navy)}
.step:nth-child(2),.step:nth-child(3){background:var(--navy-2)}
.step-title{display:flex;align-items:center;gap:8px;font-size:9.5px;font-weight:500;line-height:1.1;margin-bottom:18px}
.step p{font-size:8.8px;line-height:1.3}
.icon{width:22px;height:22px;flex:none}
.band{position:absolute;left:0;top:826px;width:680px;height:136px;background:var(--navy)}
.band-tab{position:absolute;left:116px;top:813px;background:var(--yellow);color:var(--navy);font-size:6.5px;font-weight:500;padding:3px 6px}
.chart{position:absolute;left:40px;top:832px}
.gauge{position:absolute;top:858px;width:120px;text-align:center;color:#fff}
.gauge svg{display:block;margin:0 auto}
.gauge span{display:block;font-size:9px;font-weight:500;margin-top:8px}
.gauge-a{left:368px}
.gauge-b{left:504px}
.front-rule-top{left:48px;top:0;width:584px}
.front-rule-bottom{left:0;top:958px;width:680px}

/* back */
.card{position:absolute;left:0;top:0;width:680px;height:482px;border-bottom:1px dashed #9aa3b0}
.card-strip{left:0;top:0;width:425px;height:86px;background:linear-gradient(100deg,#2b3a55 0%,#4a587a 45%,#e7a35a 80%,#f5d8a8 100%)}
.card-strip-rule{left:0;top:86px;width:425px;height:3px}
.card-brand{position:absolute;left:34px;top:30px;background:var(--navy);padding:7px 10px;border-radius:4px}
.card-divider{position:absolute;left:425px;top:0;width:1px;height:432px;background:#b7bcc4}
.product{position:absolute;left:348px;border-radius:3px}
.product-battery{top:8px;width:32px;height:70px;background:linear-gradient(90deg,#dfe1e4,#fafafa 50%,#d4d7db)}
.product-inverter{top:110px;width:40px;height:46px;background:linear-gradient(135deg,#f5f6f7,#c9cdd2)}
.product-module{top:186px;width:38px;height:66px;background:#111}
.letter{position:absolute;left:34px;top:106px;width:300px;font-size:7.4px;line-height:1.3;text-align:justify}
.letter b{font-weight:700}
.letter p{margin-bottom:3px}
.calc-note{position:absolute;left:34px;top:226px;font-size:7.2px;line-height:1.3}
.calc-note b{font-weight:700}
.checks{position:absolute;left:34px;top:262px;display:grid;grid-template-columns:96px 106px 100px 100px;row-gap:8px;font-size:7px;text-transform:uppercase}
.checks label{display:flex;align-items:center;gap:4px}
.checks i{width:9px;height:9px;border:1px solid #555;display:inline-block}
.field{position:absolute;font-size:7.4px;border-bottom:1px solid #8a8f96;height:14px}
.stamp{position:absolute;left:610px;top:24px;width:48px;height:56px;border:1px solid #555;font-size:6.5px;text-align:center;padding-top:9px;line-height:1.15}
.address{position:absolute;left:468px;top:252px;font-size:9.6px;line-height:1.4}
.service-intro{position:absolute;left:48px;top:518px;width:196px}
.service-intro h2{font-size:18px;line-height:1.2;font-weight:500}
.service-intro p{font-size:9.4px;line-height:1.4}
.services{position:absolute;left:276px;top:520px;display:grid;grid-template-columns:180px 180px;column-gap:14px;row-gap:0}
.service{height:124px}
.service-title{display:flex;align-items:center;gap:8px;font-size:8px;font-weight:700;line-height:1.05;margin-bottom:12px}
.service p{font-size:8.3px;line-height:1.28}
.back-foot{position:absolute;left:0;top:893px;width:680px;height:65px;background:var(--navy);color:#fff}
.back-foot .cta{position:absolute;left:48px;top:16px}
.back-foot .cta strong{display:block;color:var(--yellow);font-size:13px;font-weight:700}
.back-foot .cta span{font-size:11px;font-weight:500}
.back-foot .contact{right:48px;top:14px;font-size:8px;line-height:1.35}
.back-foot .contact em{font-style:normal;color:var(--yellow)}
.back-rule{left:0;top:958px;width:680px}
</style>
</head>
<body>

<!-- Vorderseite -->
<div class="sheet-slot slot-front">
 <div class="sheet front">
  <div class="front-head">
   <div class="brand"><span class="brand-dot"></span><span class="brand-name">Lichtwerk Solar</span></div>
   <div class="contact"><b>LICHTWERK SOLAR GMBH</b><br>Lindenweg 8, 47100 Auenfeld<br>Tel.: 02841 5503120<br>www.lichtwerk-solar.de</div>
  </div>
  <div class="rule-y front-rule-top"></div>
  <div class="front-head-side"></div>
  <div class="photo hero-photo" role="img" aria-label="Freiflächen-Solarmodule im Gegenlicht der untergehenden Sonne über einer Wiese"></div>
  <div class="hero-card">
   <h1>Die Sonne Scheint,<br><span>Die Unabhängigkeit<br>Wächst.</span></h1>
   <div class="accent"></div>
  </div>
  <div class="rule-y front-hero-rule"></div>

  <section class="col col-why">
   <h2>Warum Sie sich jetzt eine<br><span>Solaranlage zulegen sollten?</span></h2>
   <div class="accent"></div>
   <h3>Photovoltaik-Förderung 2024: Das müssen Hausbesitzer jetzt wissen...</h3>
   <p>Mit dem Beschluss der Schuldenbremse werden 2024 zahlreiche Förderprogramme gestrichen. Vor allem Ausgaben aus dem Klima- und Transformationsfonds werden geringer ausfallen. Dazu gehört auch die aktuelle Solarförderung, die laut Minister Brenner gekürzt werden könnte. Experten raten: Die Anschaffung lohnt sich jetzt, solange Sie von der „steuerfreien“ Anlage profitieren können.</p>
   <h3>Bundesweite Förderung: Günstiger denn je</h3>
   <p>Für Hausbesitzer ist es gerade so attraktiv wie noch nie, in eine eigene Solaranlage zu investieren. In Deutschland wurden seit Januar 2023 einige Förderprogramme und Steuererleichterungen für private Solaranlagen festgelegt. Die Höhe und Bedingungen der Förderung ist von verschiedenen Faktoren abhängig. Dazu gehören Größe der Solaranlage, Stromverbrauch und Anbieter. Durch Steuererleichterungen müssen Hausbesitzer momentan für eine Photovoltaikanlage keine Mehrwertsteuer, Einkommensteuer und Gewerbesteuer zahlen.</p>
   <p class="lead">Die Investition lohnt sich jetzt mehr denn je.</p>
  </section>

  <section class="col col-steps">
   <h2>In vier Schritten <span>zur eigenen</span><br>Solaranlage</h2>
   <div class="accent"></div>
   <div class="steps">
    <div class="step">
     <div class="step-title"><svg class="icon" viewBox="0 0 22 22" fill="none" stroke="var(--yellow)" stroke-width="1.4"><rect x="2" y="5" width="12" height="13" rx="2"/><path d="M14 8h4a2 2 0 0 1 2 2v6l-3-2h-3"/></svg>Beratung</div>
     <p>Genießen Sie den Ertrag Ihrer neuen Solaranlage. Wir übernehmen die Fernwartung nach Inbetriebnahme.</p>
    </div>
    <div class="step">
     <div class="step-title"><svg class="icon" viewBox="0 0 22 22" fill="none" stroke="var(--yellow)" stroke-width="1.4"><rect x="4" y="3" width="14" height="17" rx="1"/><path d="M8 11h6M11 8v6"/></svg>Fördermöglich<br>keiten</div>
     <p>Genießen Sie den Ertrag Ihrer neuen Solaranlage. Wir übernehmen die Fernwartung nach Inbetriebnahme.</p>
    </div>
    <div class="step">
     <div class="step-title"><svg class="icon" viewBox="0 0 22 22" fill="none" stroke="var(--yellow)" stroke-width="1.4"><path d="M4 7h14l2 9H2z"/><path d="M7 7l-1 9M11 7v9M15 7l1 9M3 11.5h16"/></svg>Planung<br>&amp; Installation</div>
     <p>Genießen Sie den Ertrag Ihrer neuen Solaranlage. Wir übernehmen die Fernwartung nach Inbetriebnahme.</p>
    </div>
    <div class="step">
     <div class="step-title"><svg class="icon" viewBox="0 0 22 22" fill="none" stroke="var(--yellow)" stroke-width="1.4"><path d="M2 17l5-9h13l-5 9z"/><path d="M9 8l-4 9M13 8l-4 9M17 8l-4 9"/></svg>Inbetriebnahme<br>&amp; Monitoring</div>
     <p>Genießen Sie den Ertrag Ihrer neuen Solaranlage. Wir übernehmen die Fernwartung nach Inbetriebnahme.</p>
    </div>
   </div>
  </section>

  <div class="band"></div>
  <div class="band-tab">Monatliche Energieproduktion und Verwendung</div>
  <svg class="chart" width="300" height="126" viewBox="0 0 300 126" aria-label="Balkendiagramm monatliche Energieproduktion">
   <g fill="#fff" font-family="Ubuntu, sans-serif" font-size="4">
    <text x="14" y="10">1.000</text><text x="14" y="40">500</text><text x="14" y="70">250</text>
    <text transform="translate(6,80) rotate(-90)">Solarstromproduktion in kWh</text>
   </g>
   <g>
    <rect x="40" y="82" width="9" height="8" fill="#b9bcc2"/><rect x="40" y="80" width="9" height="2" fill="var(--sky)"/>
    <rect x="62" y="76" width="9" height="14" fill="#b9bcc2"/><rect x="62" y="70" width="9" height="6" fill="var(--sky)"/>
    <rect x="84" y="74" width="9" height="16" fill="#b9bcc2"/><rect x="84" y="52" width="9" height="22" fill="var(--sky)"/>
    <rect x="106" y="72" width="9" height="18" fill="#b9bcc2"/><rect x="106" y="32" width="9" height="40" fill="var(--sky)"/>
    <rect x="128" y="72" width="9" height="18" fill="#b9bcc2"/><rect x="128" y="16" width="9" height="56" fill="var(--sky)"/>
    <rect x="150" y="72" width="9" height="18" fill="#b9bcc2"/><rect x="150" y="12" width="9" height="60" fill="var(--sky)"/>
    <rect x="172" y="72" width="9" height="18" fill="#b9bcc2"/><rect x="172" y="12" width="9" height="60" fill="var(--sky)"/>
    <rect x="194" y="72" width="9" height="18" fill="#b9bcc2"/><rect x="194" y="20" width="9" height="52" fill="var(--sky)"/>
    <rect x="216" y="72" width="9" height="18" fill="#b9bcc2"/><rect x="216" y="40" width="9" height="32" fill="var(--sky)"/>
    <rect x="238" y="74" width="9" height="16" fill="#b9bcc2"/><rect x="238" y="58" width="9" height="16" fill="var(--sky)"/>
    <rect x="260" y="78" width="9" height="12" fill="#b9bcc2"/><rect x="260" y="72" width="9" height="6" fill="var(--sky)"/>
    <rect x="282" y="82" width="9" height="8" fill="#b9bcc2"/><rect x="282" y="80" width="9" height="2" fill="var(--sky)"/>
   </g>
   <polyline points="44,80 66,70 88,50 110,30 132,14 154,10 176,10 198,18 220,38 242,56 264,70 286,80" fill="none" stroke="var(--yellow)" stroke-width="1.2"/>
   <line x1="34" y1="90" x2="296" y2="90" stroke="#fff" stroke-width=".4"/>
   <g fill="#fff" font-family="Ubuntu, sans-serif" font-size="4" text-anchor="middle">
    <text x="44" y="98">Jan</text><text x="66" y="98">Feb</text><text x="88" y="98">Mar</text><text x="110" y="98">Apr</text><text x="132" y="98">Mai</text><text x="154" y="98">Jun</text><text x="176" y="98">Jul</text><text x="198" y="98">Aug</text><text x="220" y="98">Sep</text><text x="242" y="98">Okt</text><text x="264" y="98">Nov</text><text x="286" y="98">Dez</text>
   </g>
   <g font-family="Ubuntu, sans-serif" font-size="4" fill="#fff">
    <rect x="70" y="108" width="10" height="2" fill="#b9bcc2"/><text x="82" y="110">Direktverbrauch</text>
    <rect x="120" y="108" width="10" height="2" fill="#8d9096"/><text x="132" y="110">Eigenverbrauch durch Batterie</text>
    <rect x="192" y="108" width="10" height="2" fill="var(--sky)"/><text x="204" y="110">Netzeinspeisung</text>
    <rect x="238" y="108" width="10" height="2" fill="var(--yellow)"/><text x="250" y="110">Energieproduktion</text>
   </g>
  </svg>
  <div class="gauge gauge-a">
   <svg width="76" height="76" viewBox="0 0 76 76"><circle cx="38" cy="38" r="34" fill="#fff"/><circle cx="38" cy="38" r="32" fill="none" stroke="var(--yellow)" stroke-width="5" stroke-dasharray="172.9 201" transform="rotate(-90 38 38)"/><text x="38" y="42" text-anchor="middle" font-family="Ubuntu, sans-serif" font-weight="700" font-size="13" fill="var(--ink)">86%</text></svg>
   <span>Unabhängigkeitsgrad</span>
  </div>
  <div class="gauge gauge-b">
   <svg width="76" height="76" viewBox="0 0 76 76"><circle cx="38" cy="38" r="34" fill="#fff"/><circle cx="38" cy="38" r="32" fill="none" stroke="var(--sky)" stroke-width="5" stroke-dasharray="78.4 201" transform="rotate(-90 38 38)"/><text x="38" y="42" text-anchor="middle" font-family="Ubuntu, sans-serif" font-weight="700" font-size="13" fill="var(--ink)">39%</text></svg>
   <span>Eigenverbrauch</span>
  </div>
  <div class="rule-y front-rule-bottom"></div>
 </div>
</div>

<!-- Rückseite mit Antwortkarte -->
<div class="sheet-slot slot-back">
 <div class="sheet back">
  <div class="card">
   <div class="photo card-strip" role="img" aria-label="Dachmodule im Abendlicht"></div>
   <div class="rule-y card-strip-rule"></div>
   <div class="card-brand brand"><span class="brand-dot"></span><span class="brand-name">Lichtwerk Solar</span></div>
   <div class="product product-battery" role="img" aria-label="Produktfoto QVR Batteriespeicher"></div>
   <div class="product product-inverter" role="img" aria-label="Produktfoto Helvorn Wechselrichter"></div>
   <div class="product product-module" role="img" aria-label="Produktfoto KE-Lumin Full-Black-Modul"></div>
   <div class="card-divider"></div>

   <div class="letter">
    <p><b>Sehr geehrte Damen und Herren,</b><br>mit einer Photovoltaikanlage auf dem Dach produzieren Sie kostengünstig „grünen Strom“ für Ihren Eigenverbrauch, leisten nebenbei noch einen wichtigen Beitrag zum Klimaschutz und senken dauerhaft Ihre Energiekosten.</p>
    <p>Mit unserer mehr als 10-jährigen Erfahrung in der Beratung, Planung, Montage und Wartung von über 2.500 Photovoltaikanlagen für Privat- und Industriekunden stellen wir eine individuelle und bedarfsgerechte Planung Ihrer Photovoltaikanlage sicher. Wir beschäftigen eigene PV-Gutachter, Dachdeckermeister, Elektromeister sowie Elektroingenieure und begleiten somit Ihr Projekt von A bis Z und das alles aus einer Hand!</p>
   </div>
   <div class="calc-note"><b>In nur 2 Minuten zur PV-Anlage!</b><br>Nutzen Sie unseren Rechner und erhalten Sie direkt einen<br>Kostenvoranschlag inkl. Wirtschaftlichkeitsberechnung.</div>

   <div class="checks">
    <label><i></i>Eigenheim</label><label><i></i>Gewerbeimmobilie</label><label><i></i>Landwirtschaft</label><label><i></i>Service &amp; Wartung</label>
    <label><i></i>Volleinspeisung</label><label><i></i>Eigenverbrauch</label><label><i></i>Batterie</label><label><i></i>Reinigung</label>
   </div>

   <div class="field" style="left:34px;top:302px;width:86px">Vorname</div>
   <div class="field" style="left:134px;top:302px;width:140px">Nachname</div>
   <div class="field" style="left:286px;top:302px;width:126px">Firma</div>
   <div class="field" style="left:34px;top:352px;width:86px">PLZ</div>
   <div class="field" style="left:134px;top:352px;width:140px">Ort</div>
   <div class="field" style="left:286px;top:352px;width:126px">Straße</div>
   <div class="field" style="left:34px;top:402px;width:240px">Tel.:</div>
   <div class="field" style="left:286px;top:402px;width:126px">E-Mail</div>
   <div class="field" style="left:34px;top:430px;width:378px">Empfehlung von</div>

   <div class="stamp">Entgelt<br>zahlt<br>Empfänger</div>
   <div class="address">Lichtwerk Solar GmbH<br>Lindenweg 8<br>47100 Auenfeld</div>
  </div>

  <section class="service-intro">
   <h2>Solaranlagen Rundum Service</h2>
   <div class="accent"></div>
   <p>Der Bau einer Solaranlage ist nicht nur kosteneffizient, sondern lohnt sich heutzutage noch mehr denn je. Sparen Sie mit uns, der Lichtwerk Solar GmbH bares Geld für den Bau Ihrer Photovoltaikanlage. Wir übernehmen für Sie ab unserer ersten Beratung sowohl die Behördengänge, den Aufbau Ihrer Photovoltaikanlage mit allen Anschlüssen als auch die Betreuung durch Monitoring. Als Marktführer für Solaranlagen-Projekte bieten wir Ihnen nach der Inbetriebnahme einen Rundum-Service an: Sie wählen Ihr Rundum-Paket aus unseren angebotenen Bausteinen aus, zum Beispiel Wartungsvertrag – Betriebsführungsvertrag – mit und ohne Reinigung – Sachversicherungen für das erste Jahr oder länger fristig.</p>
  </section>

  <div class="services">
   <div class="service">
    <div class="service-title"><svg class="icon" viewBox="0 0 22 22" fill="none" stroke="var(--yellow)" stroke-width="1.4"><circle cx="8" cy="9" r="4"/><circle cx="15" cy="15" r="3"/><path d="M8 3v2M8 13v2M2 9h2M12 9h2"/></svg>PHOTOVOLTAIK-ANLAGEN<br>BAUEN</div>
    <p>Wir installieren Ihre Solaranlage fachmännisch. Unser Beratungsservice bietet Ihnen eine genaue Planung Ihrer Solaranlage – selbstverständlich mit Ortstermin.</p>
   </div>
   <div class="service">
    <div class="service-title"><svg class="icon" viewBox="0 0 22 22" fill="none" stroke="var(--yellow)" stroke-width="1.4"><rect x="3" y="6" width="16" height="13"/><path d="M7 6v13M11 6v13M15 6v13M3 12h16M8 2l3 3 3-3"/></svg>PHOTOVOLTAIK-ANLAGEN<br>WARTEN</div>
    <p>Nachdem Ihre Solaranlage in Betrieb genommen wurde, benötigen Sie einen Wartungsservice. Mit uns an Ihrer Seite erfüllt Ihre PV-Anlage z. B. die Vorgaben der VDE-Messungen.</p>
   </div>
   <div class="service">
    <div class="service-title"><svg class="icon" viewBox="0 0 22 22" fill="none" stroke="var(--yellow)" stroke-width="1.4"><path d="M5 7h12l-1 13H6z"/><path d="M3 7h16M9 4h4M9 10v7M13 10v7"/></svg>PHOTOVOLTAIK-ANLAGEN<br>REINIGEN</div>
    <p>Unsere hochwertigen Solaranlagen laufen am besten, wenn sie sauber sind. Nutzen Sie unseren Rundum-Reinigungsservice für Ihre PV-Anlage, damit die Energie fließen kann.</p>
   </div>
   <div class="service">
    <div class="service-title"><svg class="icon" viewBox="0 0 22 22" fill="none" stroke="var(--yellow)" stroke-width="1.4"><rect x="2" y="4" width="15" height="14" rx="1"/><path d="M2 8h15M6 2v4M13 2v4"/><circle cx="17" cy="16" r="4" fill="var(--paper)"/><path d="M17 14v2l1 1"/></svg>BETRIEBSFÜHRUNG</div>
    <p>Die Software bietet Ihnen Einblicke in den Betrieb Ihrer Solaranlage. Sehen Sie die Statistik zu Verbrauch und Ertrag mit wenigen Klicks jederzeit online über unseren Login.</p>
   </div>
   <div class="service">
    <div class="service-title"><svg class="icon" viewBox="0 0 22 22" fill="none" stroke="var(--yellow)" stroke-width="1.4"><path d="M3 10l8-7 8 7v10H3z"/><path d="M8 13l6 5M14 13l-6 5"/></svg>SANIERUNG</div>
    <p>Ist Ihre Solaranlage in die Jahre gekommen oder gab es äußere Einflüsse, die zu Schäden geführt haben? Dann sanieren wir nicht nur Teile, sondern auch komplette PV-Anlagen.</p>
   </div>
   <div class="service">
    <div class="service-title"><svg class="icon" viewBox="0 0 22 22" fill="none" stroke="var(--yellow)" stroke-width="1.4"><path d="M3 3v16h16"/><path d="M6 15l4-5 3 3 5-7"/></svg>GUTACHTEN ERSTELLEN</div>
    <p>Als zertifiziertes Unternehmen erstellen wir Gutachten. Wir übernehmen sämtliche Gutachter-Tätigkeiten rund um Ihre Solaranlage bei Defekt oder Garantiefragen.</p>
   </div>
  </div>

  <footer class="back-foot">
   <div class="cta"><strong>BERATUNG GEWÜNSCHT?</strong><span>Rufen Sie uns an: 02841 5503120</span></div>
   <div class="contact"><b>LICHTWERK SOLAR GMBH</b><br>Lindenweg 8, 47100 Auenfeld | Tel.: 02841 5503120<br><em>www.lichtwerk-solar.de</em></div>
  </footer>
  <div class="rule-y back-rule"></div>
 </div>
</div>

</body>
</html>
```